Microblading website contest - Make it colorful

Beauty salon focusing on microblading need a better website template. Please make a 1 page site mobile optimized and nicer layout with better color formulation. Would love interactive images in the site. You can use stock images and if approve we can pay for it.
Current site:
nerisapetalloft.example

Inspiration:
https://quorvelle.example/shots/48112096-Microblading-HomePage
https://quorvelle.example/shots/7104529-Fernwick-Microblading-Eyebrow-Beauty-Salon-WordPress-Theme

Target Market(s)

women

Industry/Entity Type

beauty salon

Number of Pages Required

1 page

Font styles to use
Serif
Decorative
Script

Requirements
Nice to have
• As pretty as possible

```html
<!DOCTYPE html>
<html lang="en">
<head>
<meta charset="utf-8">
<title>Nerisa Petal Loft – Microblading</title>
<link href="https://fonts.googleapis.com/css2?family=Great+Vibes&family=Questrial&display=swap" rel="stylesheet">
<style>
:root{
  --blue:#4fc4e4;
  --magenta:#cf57ea;
  --ink:#1d1d1d;
  --muted:#7a7a7a;
  --faint:#b9b9c4;
  --hero:#f7ebf6;
  --band:#e9dde7;
  --rule:#6fb8d8;
  --script:"Great Vibes",cursive;
  --sans:"Questrial",sans-serif;
}
*{margin:0;padding:0;box-sizing:border-box}
html,body{width:1200px;height:3343px;overflow:hidden;background:#fff}
body{position:relative;font-family:var(--sans);color:var(--ink)}
.abs{position:absolute}
.topbar{top:0;left:0;width:1200px;height:41px;background:#fff}
.topbar .addr{left:183px;top:14px;font-size:12px}
.socials{left:810px;top:10px;display:flex;gap:14px}
.socials span{width:21px;height:21px;border-radius:50%;background:#111;display:block}
.cart{left:966px;top:12px;font-size:12px;font-weight:bold;display:flex;gap:8px;align-items:center}
.hero{top:41px;left:0;width:1200px;height:635px;background:var(--hero);overflow:hidden}
.brand{left:183px;top:30px;font-size:20px;color:var(--ink)}
.nav{left:412px;top:38px;display:flex;gap:18px;font-size:13px}
.hero-title{right:186px;top:270px;font-family:var(--script);font-size:82px;white-space:nowrap;
  background:linear-gradient(90deg,var(--blue),#8a7de8 45%,var(--magenta));-webkit-background-clip:text;background-clip:text;color:transparent}
.hero-sub{right:186px;top:367px;font-size:13px}
.btn{display:flex;align-items:center;justify-content:center;border-radius:30px;font-size:13px}
.btn-fill{background:var(--blue);color:#fff}
.btn-line{border:1.5px solid var(--blue);color:var(--blue);background:transparent}
.script-h{font-family:var(--script);color:var(--blue);white-space:nowrap}
.about p{font-size:12.5px;line-height:20px;margin-bottom:16px}
.about p.soft{color:var(--muted)}
.band{left:0;width:1200px}
.feature{width:280px;text-align:center}
.feature .ring{width:108px;height:108px;margin:0 auto}
.feature h3{font-weight:normal;font-size:16px;margin-top:22px;letter-spacing:.3px}
.feature p{font-size:12.5px;line-height:20px;margin-top:14px}
.centered{left:0;width:1200px;text-align:center}
.svc h3{font-weight:normal;font-size:15px}
.svc .line1{font-size:12.5px;margin-top:10px;line-height:20px}
.svc .line2{font-size:12px;color:var(--faint);margin-top:6px}
.svc{left:332px;width:536px;text-align:center;border-bottom:1.5px solid var(--rule);padding-bottom:10px}
.contact-row{left:465px;display:flex;align-items:center;gap:14px;font-size:12.5px}
.contact-row span.dot{width:35px;height:35px;border-radius:50%;background:#111;display:block}
.footer{font-size:12.5px}
</style>
</head>
<body>

<div class="abs topbar">
  <div class="abs addr">2870 Marrow Ave #114, Queens, NY 11360</div>
  <div class="abs socials"><span></span><span></span><span></span><span></span></div>
  <div class="abs cart">
    <svg width="18" height="15" viewBox="0 0 18 15"><path d="M0 1h3l2 8h10l2-6H5" fill="none" stroke="#111" stroke-width="2"/><circle cx="6" cy="13" r="1.6" fill="#111"/><circle cx="14" cy="13" r="1.6" fill="#111"/></svg>
    Cart
  </div>
</div>

<section class="abs hero">
  <svg class="abs" style="left:0;top:0" width="1200" height="635" viewBox="0 0 1200 635">
    <path d="M560 0 C700 40 620 200 760 210 C900 220 960 40 1080 0 Z" fill="#f1e2ee"/>
    <circle cx="-20" cy="180" r="60" fill="none" stroke="#e3ecf7" stroke-width="14"/>
    <circle cx="58" cy="370" r="22" fill="#f0dff0"/>
    <circle cx="1120" cy="540" r="160" fill="none" stroke="#f0e0ee" stroke-width="14"/>
    <g role="img" aria-label="Close-up photo of a woman with eyes closed showing defined eyebrows">
      <defs><linearGradient id="heroPhoto" x1="0" y1="0" x2="1" y2="1">
        <stop offset="0" stop-color="#e7c2b3"/><stop offset=".6" stop-color="#d29b88"/><stop offset="1" stop-color="#3a2421"/></linearGradient></defs>
      <path d="M0 460 C0 340 80 100 230 110 C360 120 460 160 420 330 C390 460 420 560 370 635 L0 635 Z" fill="url(#heroPhoto)"/>
    </g>
  </svg>
  <div class="abs brand">Nerisa Petal Loft</div>
  <nav class="abs nav"><span>Home</span><span>About</span><span>Services</span><span>Gallery</span><span>Shop</span><span>Academy</span><span>Contact Us</span><span>Customer Feedback</span><span>More</span></nav>
  <h1 class="abs hero-title" style="font-weight:normal">Petal Loft Nerisa</h1>
  <div class="abs hero-sub">Your Personal Eyebrow Specialist</div>
  <a class="abs btn btn-fill" style="left:747px;top:403px;width:126px;height:40px">Services</a>
  <a class="abs btn btn-line" style="left:891px;top:403px;width:125px;height:40px">Contact Us</a>
</section>

<section class="abs about" style="top:676px;left:0;width:1200px;height:661px">
  <svg class="abs" style="left:0;top:0" width="1200" height="661">
    <circle cx="0" cy="230" r="97" fill="#f7eef4"/>
    <circle cx="1290" cy="290" r="215" fill="#faf2f6"/>
    <circle cx="505" cy="545" r="27" fill="#f7eaf2"/>
    <rect role="img" aria-label="Portrait photo of the smiling brow artist" x="214" y="128" width="285" height="389" rx="142" fill="#e8cfe3"/>
  </svg>
  <h2 class="abs script-h" style="left:562px;top:110px;font-size:66px;font-weight:normal">Hi, I'm Nerisa!</h2>
  <div class="abs" style="left:564px;top:205px;width:500px">
    <p class="soft">Nerisa has 7 years of microblading experience. She graduated from LumaStroke United States. After, she studied in Velora Academy, a global top brand from Germany. She was personally guided by the brand CEO Anton Reslav and the first China Master Mei Tovan.</p>
    <p>After earning award of VeloBrows Artist in 2019. Nerisa continued her practice microblading until she won the world's first VeloBrows Master in Taiwan in 2021. She is currently the only certificated Master technician in Taiwan. She also holds a shading and VeloGlow Master.</p>
    <p class="soft">On Nerisa's microblading journey. She travelled to places all over the world and met mentors on her path. She was willing to learn any new tech and inspire a better self regardless how much the cost was.</p>
    <p>Today, Nerisa has become one of the very successful eyebrow tattoo artists in New York. No matter what the eyebrow trend is, Nerisa focuses on how to provide an exclusive and the most suitable eyebrow for each clients.</p>
  </div>
</section>

<section class="abs band" style="top:1337px;height:564px;background:linear-gradient(100deg,#ece1ea,#e3d5e1 50%,#eee3ec)" role="img" aria-label="Soft pink background photo of an eyebrow treatment">
  <h2 class="abs script-h centered" style="top:38px;font-size:68px;font-weight:normal">Your Eyebrows &amp; Beauty</h2>
  <div class="abs centered" style="top:125px;font-size:15px;letter-spacing:.5px">LET US TAKE CARE OF IT</div>
  <svg width="0" height="0" class="abs"><defs><linearGradient id="ring" x1="0" y1="0" x2="0" y2="1"><stop offset="0" stop-color="#cf57ea"/><stop offset="1" stop-color="#4fc4e4"/></linearGradient></defs></svg>
  <div class="abs feature" style="left:166px;top:191px">
    <svg class="ring" viewBox="0 0 108 108"><circle cx="54" cy="54" r="52" fill="none" stroke="url(#ring)" stroke-width="2.5"/><path d="M30 60 Q52 44 76 58 M34 63 l-4 6 M42 66 l-2 7 M51 67 v7 M60 66 l2 7" stroke="url(#ring)" stroke-width="2.5" fill="none"/><path d="M30 42 Q52 30 80 38" stroke="url(#ring)" stroke-width="3" fill="none"/></svg>
    <h3>LICENSED MICROBLADING ARTIST</h3>
    <p>License from various states in<br>The United States</p>
  </div>
  <div class="abs feature" style="left:459px;top:191px">
    <svg class="ring" viewBox="0 0 108 108"><circle cx="54" cy="54" r="52" fill="none" stroke="url(#ring)" stroke-width="2.5"/><path d="M38 40 l3 7 7 1-5 5 1 7-6-3-6 3 1-7-5-5 7-1z M62 26 l2 5 5 1-4 3 1 5-4-2-4 2 1-5-4-3 5-1z" fill="none" stroke="url(#ring)" stroke-width="2"/><path d="M58 78 V50 a3 3 0 0 1 6 0 V62 h8 a4 4 0 0 1 4 4 v12" fill="none" stroke="url(#ring)" stroke-width="2.5"/></svg>
    <h3>YEARS OF EXPERIENCE</h3>
    <p>Over thousands of cases<br>Oversea study and practice</p>
  </div>
  <div class="abs feature" style="left:751px;top:191px">
    <svg class="ring" viewBox="0 0 108 108"><circle cx="54" cy="54" r="52" fill="none" stroke="url(#ring)" stroke-width="2.5"/><rect x="28" y="32" width="52" height="36" rx="3" fill="none" stroke="url(#ring)" stroke-width="2.5"/><path d="M48 68 l-4 10 h20 l-4-10" fill="none" stroke="url(#ring)" stroke-width="2.5"/><circle cx="54" cy="48" r="6" fill="none" stroke="url(#ring)" stroke-width="2"/></svg>
    <h3>LATEST EUROPEAN TECHNIQUE</h3>
    <p>We study European-style natural hair flow,<br>improve and make it suitable for Asians</p>
  </div>
  <a class="abs btn btn-line" style="left:515px;top:435px;width:169px;height:48px;font-size:15px">SHOW MORE</a>
</section>

<section class="abs" style="top:1901px;left:0;width:1200px;height:892px;overflow:hidden">
  <svg class="abs" style="left:0;top:0" width="1200" height="892">
    <defs>
      <linearGradient id="leftPhoto" x1="0" y1="0" x2="1" y2="0"><stop offset="0" stop-color="#e6dcdf"/><stop offset="1" stop-color="#fff" stop-opacity="0"/></linearGradient>
      <radialGradient id="flowers"><stop offset="0" stop-color="#f1cfd3"/><stop offset="1" stop-color="#fff" stop-opacity="0"/></radialGradient>
    </defs>
    <rect role="img" aria-label="Faint photo of a technician in gloves working on a client's brows" x="0" y="360" width="460" height="532" fill="url(#leftPhoto)"/>
    <ellipse role="img" aria-label="Faint decorative photo of pink blossoms" cx="1110" cy="170" rx="190" ry="200" fill="url(#flowers)"/>
  </svg>
  <h2 class="abs script-h centered" style="top:70px;font-size:68px;font-weight:normal">Specialized Service</h2>
  <div class="abs centered" style="top:150px;font-size:16px;line-height:20px">We treat every client as our friends and family. We give you the<br>most sincere advise and best quality and service.<br><br>We do not only follow the trend. We hear you, and want you to<br>love it forever.</div>
  <div class="abs svc" style="top:336px"><h3>NATURAL BROWS</h3><div class="line1">Microblading | Hand-drawing hair lines</div><div class="line2">For all skin types</div></div>
  <div class="abs svc" style="top:473px"><h3>POWDER EYELINER (NATURAL EYESHADOW)</h3><div class="line1">Extend eyeline at end of the eye| With a touch of ligh eyeshadow vision</div><div class="line2">For those who like to have an eye makeup filter 24/7 | Eye-shape adjustment</div></div>
  <div class="abs svc" style="top:600px"><h3>SCALP MICROPIGMENTATION</h3><div class="line1">Add destiny to the thinning area | Seamless and Undetectable |<br>Accommodates your skin tone and natural hair color | providing the appearance of hair</div><div class="line2">For restoring hairline | Bald spots | Scar covering</div></div>
  <a class="abs btn btn-line" style="left:515px;top:759px;width:169px;height:48px;font-size:15px">SERVICES</a>
</section>

<section class="abs band" style="top:2793px;height:410px;background:linear-gradient(180deg,#e0d2dc,#e6dae4)" role="img" aria-label="Soft faded background photo of a woman's eyes">
  <h2 class="abs script-h centered" style="top:20px;font-size:68px;font-weight:normal">More Services</h2>
  <div class="abs contact-row" style="top:115px"><span class="dot"></span>Snapframe - nerisapetalloftvelomaster</div>
  <div class="abs contact-row" style="top:165px"><span class="dot"></span>Friendbook - nerisapetalloft</div>
  <div class="abs contact-row" style="top:216px"><span class="dot"></span>Pingtalk - @nerisabrows</div>
  <div class="abs contact-row" style="top:266px"><span class="dot"></span>Chatwell - nerisabrows</div>
  <a class="abs btn btn-line" style="left:515px;top:331px;width:169px;height:48px;font-size:15px">CONTACT US</a>
</section>

<footer class="abs footer centered" style="top:3203px;height:140px">
  <div class="abs centered" style="top:34px">2870 Marrow Ave #114, Queens, NY 11360</div>
  <div class="abs centered" style="top:54px">Nerisa Petal Loft Inc</div>
  <div class="abs centered" style="top:93px">This website is created by NerisaPetalLoft &nbsp;|&nbsp; Copyright 2015</div>
</footer>

</body>
</html>
```